fieldscoutingpath.com - Social Media Branding

fieldscoutingpath.com --> Social Media Re-Branding & Graphics
Facebook: @fldscoutpath - Instagram: @fieldscoutingpath - Twitter: @fldscoutpath

Looking to find a good designer to help with my fieldscoutingpath.com social media sites!
- facebook banner
- twitter banner
- instagram template (square and banner size)
- Quote or Information Template
- Committed Template (uniformed) - see the ones I made (& i am no professional) at fieldscoutingpath.com/committed - needs to have fieldscoutingpath.com logo, room for: the committed school and the team the player plays on.

Also willing to pay extra for a graphic that is the "complete package" that detail all of the steps of the recruiting process detailed in fieldscoutingpath.com

Font styles to use
Sans Serif

Colors
ec1f27
fbee3e

```html
<!DOCTYPE html>
<html lang="en">
<head>
<meta charset="utf-8">
<title>fieldscoutingpath.com – Free Recruiting Seminar</title>
<link rel="stylesheet" href="https://fonts.googleapis.com/css2?family=Roboto:wght@400;700;900&display=swap">
<style>
  :root {
    --brand-red: #ec1f27;
    --brand-yellow: #fbee3e;
    --wave-white: #ffffff;
    --ink: #141414;
    --text-light: #ffffff;
    --ball-light: #e4f23a;
    --ball-dark: #5f7a0e;
  }
  * { margin: 0; padding: 0; box-sizing: border-box; }
  html, body { width: 1200px; height: 1200px; overflow: hidden; background: var(--brand-red); }
  .poster {
    position: relative;
    width: 1200px;
    height: 1200px;
    overflow: hidden;
    font-family: "Roboto", Arial, sans-serif;
    background: var(--brand-red);
  }
  .poster-background { position: absolute; inset: 0; }
  .brand {
    position: absolute;
    top: 52px;
    left: 0;
    right: 0;
    display: flex;
    justify-content: center;
    align-items: center;
    gap: 22px;
  }
  .brand-mark {
    width: 44px;
    height: 44px;
    border-radius: 50%;
    background: var(--brand-yellow);
  }
  .brand-name {
    color: var(--text-light);
    font-weight: 700;
    font-size: 40px;
    letter-spacing: 0.2px;
    padding-bottom: 8px;
    border-bottom: 2px solid var(--text-light);
  }
  .headline {
    position: absolute;
    top: 184px;
    left: 0;
    right: 0;
    text-align: center;
    color: var(--text-light);
    font-weight: 700;
    font-size: 74px;
    letter-spacing: -0.5px;
  }
  .audience {
    position: absolute;
    top: 294px;
    left: 0;
    right: 0;
    text-align: center;
    color: var(--text-light);
    font-weight: 400;
    font-size: 49px;
  }
  .event-time {
    position: absolute;
    left: 44px;
    top: 1030px;
    color: var(--ink);
    font-weight: 700;
    font-size: 58px;
    line-height: 1.08;
    letter-spacing: -1px;
  }
  .social-links {
    position: absolute;
    right: 45px;
    top: 1077px;
    display: flex;
    gap: 21px;
  }
  .social-dot {
    width: 72px;
    height: 72px;
    border-radius: 50%;
    background: var(--ink);
  }
</style>
</head>
<body>
  <main class="poster">
    <svg class="poster-background" width="1200" height="1200" viewBox="0 0 1200 1200" xmlns="http://www.w3.org/2000/svg">
      <defs>
        <radialGradient id="softball-fill" cx="0.42" cy="0.38" r="0.65">
          <stop offset="0" stop-color="#f3fb8a"/>
          <stop offset="0.45" stop-color="var(--ball-light)"/>
          <stop offset="1" stop-color="var(--ball-dark)"/>
        </radialGradient>
      </defs>
      <rect class="sky-band" width="1200" height="1200" fill="var(--brand-red)"/>
      <path class="wave-edge" d="M0 676 C180 650 330 700 520 730 C720 762 900 755 1200 736 L1200 1200 L0 1200 Z" fill="var(--wave-white)"/>
      <path class="ground-band" d="M0 694 C180 668 330 718 520 748 C720 780 900 773 1200 754 L1200 1200 L0 1200 Z" fill="var(--brand-yellow)"/>
      <g class="accent-lines" stroke="var(--brand-yellow)" stroke-width="2.5" fill="none">
        <line x1="0" y1="176" x2="114" y2="91"/>
        <circle cx="128" cy="81" r="13"/>
        <line x1="1200" y1="262" x2="1003" y2="447"/>
        <circle cx="990" cy="460" r="13"/>
      </g>
      <circle class="softball" role="img" aria-label="Illustration of a yellow softball with red stitching" cx="612" cy="713" r="284" fill="url(#softball-fill)"/>
    </svg>

    <header class="brand">
      <span class="brand-mark"></span>
      <span class="brand-name">fieldscoutingpath.com</span>
    </header>

    <h1 class="headline">Free Recruiting Seminar</h1>
    <p class="audience">Player, Parents &amp; Coaches</p>

    <p class="event-time">Wednesday<br>7PM ET</p>

    <nav class="social-links" aria-label="Social media">
      <span class="social-dot"></span>
      <span class="social-dot"></span>
      <span class="social-dot"></span>
    </nav>
  </main>
</body>
</html>
```